Industrial Services company needs a business card design

We provide industrial maintenance services including sandblasting, painting, pressure washing, storage tank rehabilitation, and welding. I would like an industrial design that's eye catching. I would like the back-side of the card to list our services.

Industry/Entity Type

Construction

Contact Information for Business Card

address: 418 Hartwell Lane, York, PA 17405
Phone: 410-637-4815
email: corvethinc@mailbrook.net
Daniel Verhoeven, President
www.corvethcoating.net

Logo Text

Corveth Industrial Services

Font styles to use
Sans Serif

Colors
000000
229ed3
0692cd
ffffff

Requirements
Must have
• Easy to read
• our services listed/included on back of card
• eye catching color combinations
Nice to have
• Water storage tank image

```html
<!DOCTYPE html>
<html lang="en">
<head>
<meta charset="utf-8">
<title>Corveth Inc – Business Card</title>
<link rel="stylesheet" href="https://fonts.googleapis.com/css2?family=Lato:wght@400;700;900&display=swap">
<style>
  :root {
    --ink: #000000;
    --blue: #0692cd;
    --blue-light: #229ed3;
    --blue-deep: #0a86c4;
    --white: #ffffff;
    --grey: #6d6e71;
    --text-dark: #2b2b2b;
    --stage: #e9ecef;
  }
  * { margin: 0; padding: 0; box-sizing: border-box; }
  html, body {
    width: 1200px; height: 900px; overflow: hidden;
    background: var(--stage);
    font-family: "Lato", Arial, sans-serif;
  }
  .canvas { position: relative; width: 1200px; height: 900px; }

  .card { position: absolute; overflow: hidden; box-shadow: 0 6px 18px rgba(0,0,0,.18); }

  /* Back side: contact and services */
  .card-back {
    left: 177px; top: 74px; width: 589px; height: 364px;
    background: var(--blue-deep); color: var(--white);
  }
  .card-back .accent-disc {
    position: absolute; left: 360px; top: 72px;
    width: 360px; height: 360px; border-radius: 50%;
    background: var(--blue-light);
  }
  .card-back .white-disc {
    position: absolute; left: 382px; top: 94px;
    width: 316px; height: 316px; border-radius: 50%;
    background: var(--white);
  }
  .contact { position: absolute; left: 24px; top: 38px; }
  .contact .name { font-size: 21px; font-weight: 400; letter-spacing: .3px; line-height: 1; }
  .contact .role { font-size: 16px; margin-top: 4px; }
  .contact .address { font-size: 16px; line-height: 22px; margin-top: 10px; }
  .contact .lines { list-style: none; margin-top: 10px; font-size: 16px; line-height: 22px; }
  .contact .lines li { display: flex; align-items: center; gap: 3px; }
  .contact .lines svg { width: 13px; height: 13px; fill: var(--white); }
  .services { position: absolute; left: 23px; top: 222px; width: 228px; }
  .services .heading { display: flex; align-items: center; font-size: 15px; }
  .services .heading::after { content: ""; flex: 1; height: 1px; background: rgba(255,255,255,.6); margin-left: 2px; }
  .services ul { list-style: none; margin-top: 12px; }
  .services li { font-size: 13px; font-weight: 700; line-height: 22px; display: flex; align-items: center; gap: 6px; }
  .services li::before { content: ""; width: 8px; height: 8px; border-radius: 50%; background: var(--white); }

  /* Front side: name and tagline */
  .card-front {
    left: 388px; top: 505px; width: 567px; height: 352px;
    background: var(--white); text-align: center;
  }
  .brand-dot {
    position: absolute; left: 258px; top: 72px;
    width: 52px; height: 52px; border-radius: 50%; background: var(--blue-light);
  }
  .brand-name {
    position: absolute; left: 0; right: 0; top: 170px;
    font-size: 46px; font-weight: 900; color: var(--blue); letter-spacing: 1px; line-height: 1;
  }
  .brand-line {
    position: absolute; left: 0; right: 0; top: 222px;
    font-size: 17px; font-weight: 900; color: var(--grey); letter-spacing: .3px;
  }
  .divider { position: absolute; left: 88px; right: 88px; top: 268px; height: 1px; background: #888; }
  .offer {
    position: absolute; left: 0; right: 0; top: 278px;
    font-size: 13px; font-weight: 700; color: var(--text-dark); line-height: 17px;
  }
</style>
</head>
<body>
<main class="canvas">

  <section class="card card-back" aria-label="Card back with contact details and services">
    <div class="accent-disc"></div>
    <div class="white-disc"></div>
    <div class="contact">
      <p class="name">DANIEL VERHOEVEN</p>
      <p class="role">President</p>
      <p class="address">418 Hartwell Lane<br>York, PA 17405</p>
      <ul class="lines">
        <li><svg viewBox="0 0 16 16" aria-hidden="true"><path d="M3 2h3l1.5 3.5-2 1.2a8 8 0 0 0 3.8 3.8l1.2-2L14 10v3a1 1 0 0 1-1 1A12 12 0 0 1 2 3a1 1 0 0 1 1-1z"/></svg>410-637-4815</li>
        <li><svg viewBox="0 0 16 16" aria-hidden="true"><path d="M1 3h14v10H1z M1.5 3.5 8 9l6.5-5.5" stroke="#0a86c4" stroke-width="1.2"/></svg>corvethinc@mailbrook.net</li>
        <li><svg viewBox="0 0 16 16" aria-hidden="true"><circle cx="8" cy="8" r="7"/></svg>www.corvethcoating.net</li>
      </ul>
    </div>
    <div class="services">
      <p class="heading">OUR SERVICES:</p>
      <ul>
        <li>SANDBLASTING</li>
        <li>INDUSTRIAL PAINTING</li>
        <li>PRESSURE WASHING</li>
        <li>WELDING</li>
      </ul>
    </div>
  </section>

  <section class="card card-front" aria-label="Card front with company name">
    <div class="brand-dot"></div>
    <p class="brand-name">CORVETH INC</p>
    <p class="brand-line">COMMERCIAL &amp; INDUSTRIAL PAINTING</p>
    <div class="divider"></div>
    <p class="offer">STORAGE TANK INSPECTION, MAINTENANCE, REHABILITATION<br>REPAIR, &amp; DEMOLITION</p>
  </section>

</main>
</body>
</html>
```